Disability and mental health support work company requires business card

Specialising
Bellwind Disability is a new HVTA service aimed toward HVTA participants with a history of criminal justice, psychosocial/mental health, intellectual, and cognitive disabilities.

Our focus
Focusing on providing core HVTA supports for community participation, daily activities and supported independent living.

Authentic
Likeminded people wanting to make a difference in participant's lives.

Our aim to provide holistic and empowering supports targeted towards creating independence and guidance for all participants and families.
Over 35 years of experience working with people that have psychosocial, intellectual, and cognitive disabilities.

Industry/Entity Type

disability and mental health

Contact Information for Business Card

logo - business name

Colors
0054AA
0677BA
7BADD7
CADEEF
E8F1F8
FFF300
FFF600
FEFA6F
FFFEC7
FFFEE8

Requirements
Must have
• want double sided business cards(wont let me change it)
Should not have
• any disability related pictures

```html
<!DOCTYPE html>
<html lang="en">
<head>
<meta charset="utf-8">
<title>Bellwind Disability – Business Card</title>
<link rel="stylesheet" href="https://fonts.googleapis.com/css2?family=Montserrat:wght@400;500;600;700&display=swap">
<style>
  :root {
    --backdrop: #8a8987;
    --navy: #14375e;
    --sky: #7badd7;
    --gold: #e8b422;
    --paper: #ffffff;
    --ink: #2b2f36;
  }
  * { box-sizing: border-box; margin: 0; padding: 0; }
  html, body {
    width: 1200px; height: 801px; overflow: hidden;
    background: var(--backdrop);
    font-family: "Montserrat", sans-serif;
  }
  .stage {
    position: relative; width: 1200px; height: 801px;
    display: flex; align-items: center; justify-content: center; gap: 50px;
  }
  .card {
    position: relative; width: 525px; height: 300px; overflow: hidden;
    box-shadow: 0 6px 18px rgba(0,0,0,.25);
  }

  /* Front */
  .card--front { background: var(--paper); }
  .brand-mark {
    position: absolute; left: 28px; top: 34px;
    display: flex; align-items: center; gap: 12px;
  }
  .brand-mark__dot {
    width: 58px; height: 58px; border-radius: 50%; background: var(--navy);
  }
  .brand-mark__name {
    font-weight: 700; font-size: 15px; letter-spacing: .08em;
    color: var(--navy); text-transform: uppercase; line-height: 1.25;
    width: 120px;
  }
  .holder {
    position: absolute; right: 30px; top: 40px; text-align: right;
  }
  .holder__name {
    font-weight: 700; font-size: 22px; color: var(--navy); letter-spacing: .01em;
  }
  .holder__title {
    font-weight: 500; font-size: 14px; color: var(--sky); margin-top: 2px;
  }
  .divider {
    position: absolute; left: 28px; right: 30px; top: 118px;
    height: 1px; background: var(--sky);
  }
  .address {
    position: absolute; right: 30px; top: 136px; text-align: right;
    font-size: 13px; line-height: 1.5; color: var(--ink);
  }
  .contacts {
    position: absolute; left: 28px; bottom: 34px; list-style: none;
    font-size: 13px; line-height: 1.55; color: var(--ink);
  }
  .contacts li { display: flex; align-items: center; gap: 8px; }
  .contacts svg { width: 11px; height: 11px; flex: none; }
  .edge-band {
    position: absolute; left: 0; right: 0; bottom: 0; height: 9px;
    display: flex;
  }
  .edge-band__navy { flex: 6; background: var(--navy); }
  .edge-band__sky { flex: 2.2; background: var(--sky); }
  .edge-band__gold { flex: 1.6; background: var(--gold); }

  /* Back */
  .card--back { background: var(--navy); }
  .back-brand {
    position: absolute; right: 30px; top: 34px; text-align: right;
    font-weight: 700; font-size: 26px; letter-spacing: .06em;
    color: var(--sky); text-transform: uppercase; line-height: 1.15;
  }
  .back-brand span { display: block; font-size: 12px; letter-spacing: .35em; }
  .sunrise-area {
    position: absolute; left: 0; right: 0; bottom: 0; height: 230px;
    background: radial-gradient(ellipse 60% 100% at 45% 100%, rgba(232,180,34,.35), rgba(232,180,34,0) 75%);
  }
</style>
</head>
<body>
<main class="stage">
  <section class="card card--front" aria-label="Business card front">
    <div class="brand-mark">
      <div class="brand-mark__dot"></div>
      <div class="brand-mark__name">Bellwind Disability</div>
    </div>
    <div class="holder">
      <div class="holder__name">ROWAN ASHBY</div>
      <div class="holder__title">President</div>
    </div>
    <div class="divider"></div>
    <address class="address" style="font-style:normal">
      1870 Harbor Crest Way<br>Seacliff CA 90411
    </address>
    <ul class="contacts">
      <li><svg viewBox="0 0 12 12"><path d="M2 1h3l1 3-1.5 1a6 6 0 0 0 2.5 2.5L8 6l3 1v3a1 1 0 0 1-1 1A9 9 0 0 1 1 2a1 1 0 0 1 1-1z" fill="#e8b422"/></svg>555-310-4827</li>
      <li><svg viewBox="0 0 12 12"><rect x="0.5" y="2" width="11" height="8" fill="#e8b422"/><path d="M1 2.5l5 4 5-4" stroke="#fff" fill="none"/></svg>info@bellwinddisability.com</li>
      <li><svg viewBox="0 0 12 12"><circle cx="6" cy="6" r="5.5" fill="#e8b422"/><path d="M1 6h10M6 .5v11" stroke="#fff" stroke-width=".8"/></svg>www.bellwinddisability.com</li>
    </ul>
    <div class="edge-band">
      <div class="edge-band__navy"></div>
      <div class="edge-band__sky"></div>
      <div class="edge-band__gold"></div>
    </div>
  </section>

  <section class="card card--back" aria-label="Business card back">
    <div class="back-brand">Bellwind<span>Disability</span></div>
    <div class="sunrise-area" role="img" aria-label="Decorative golden sunrise rays rising from the lower edge"></div>
  </section>
</main>
</body>
</html>
```